Korvell Plant Services

We are a heavy diesel mechanical business with additional air con certificates, remapping engine rebuilt

Contact Information for Business Card

Company Name, Director Name, Managing Director, Contact details, email and website

Font styles to use
Serif
Script

```html
<!DOCTYPE html>
<html lang="en">
<head>
<meta charset="utf-8">
<title>Korvell Plant Services – Business Card</title>
<link rel="stylesheet" href="https://fonts.googleapis.com/css2?family=Roboto:wght@400;500;700;900&display=swap">
<style>
  :root {
    --navy: #1b1c7a;
    --navy-deep: #15166a;
    --ink: #111111;
    --paper: #ffffff;
    --stage: #2b2b2b;
    --muted: #333333;
  }
  * { margin: 0; padding: 0; box-sizing: border-box; }
  html, body { width: 1200px; height: 894px; overflow: hidden; }
  body {
    background: var(--stage);
    font-family: "Roboto", Arial, sans-serif;
    position: relative;
  }
  .card {
    position: absolute;
    width: 540px;
    height: 310px;
    overflow: hidden;
    box-shadow: 0 10px 28px rgba(0,0,0,.45);
  }

  /* Front */
  .card-front {
    left: 70px; top: 110px;
    background: var(--navy);
    color: var(--paper);
  }
  .front-brand {
    position: absolute;
    left: 0; right: 0; top: 108px;
    display: flex; align-items: center; justify-content: center; gap: 12px;
  }
  .brand-dot {
    width: 22px; height: 22px; border-radius: 50%;
    background: var(--paper);
  }
  .front-brand .brand-name {
    font-size: 30px; font-weight: 700; letter-spacing: .3px;
  }
  .front-web {
    position: absolute; left: 0; right: 0; top: 214px;
    display: flex; align-items: center; justify-content: center; gap: 10px;
    font-size: 13px; font-weight: 500;
  }
  .front-web svg { width: 14px; height: 14px; }

  /* Back */
  .card-back {
    left: 590px; top: 475px;
    background: var(--paper);
    color: var(--ink);
  }
  .back-brand {
    position: absolute; left: 30px; top: 36px;
    display: flex; align-items: center; gap: 8px;
  }
  .back-brand .brand-dot { background: var(--navy); width: 16px; height: 16px; }
  .back-brand .brand-name {
    font-size: 20px; font-weight: 700; color: var(--navy);
  }
  .machine-art {
    position: absolute; right: 40px; top: 0;
    width: 170px; height: 255px;
    background: linear-gradient(160deg, #000 0%, #1a1a1a 60%, #000 100%);
    border-radius: 6px 0 40px 0;
  }
  .edge-band {
    position: absolute; right: 0; top: 88px;
    width: 22px; height: 80px;
    background: var(--navy);
  }
  .person {
    position: absolute; left: 30px; top: 112px;
  }
  .person-name { font-size: 32px; line-height: 1; }
  .person-name .first { font-weight: 900; }
  .person-name .last { font-weight: 400; }
  .person-role {
    margin-top: 5px; font-size: 13px; color: var(--navy); font-weight: 500;
  }
  .contact-list {
    position: absolute; left: 34px; top: 188px;
    list-style: none;
    font-size: 12.5px; color: var(--muted); line-height: 1.35;
  }
  .contact-list li {
    display: flex; align-items: flex-start; gap: 12px; margin-bottom: 8px;
  }
  .contact-list svg { width: 12px; height: 12px; margin-top: 2px; flex: none; fill: var(--navy); }
</style>
</head>
<body>

<section class="card card-front" aria-label="Business card front">
  <div class="front-brand">
    <span class="brand-dot"></span>
    <span class="brand-name">Korvell Plant Services</span>
  </div>
  <div class="front-web">
    <svg viewBox="0 0 16 16" aria-hidden="true"><circle cx="8" cy="8" r="7" fill="none" stroke="#fff" stroke-width="1.4"/><path d="M1 8h14M8 1c-3 3.5-3 10.5 0 14M8 1c3 3.5 3 10.5 0 14" fill="none" stroke="#fff" stroke-width="1.2"/></svg>
    <span>korvellplantservices.net</span>
  </div>
</section>

<section class="card card-back" aria-label="Business card back">
  <div class="back-brand">
    <span class="brand-dot"></span>
    <span class="brand-name">Korvell Plant Services</span>
  </div>

  <div class="machine-art" role="img" aria-label="Black silhouette of an excavator arm and bucket"></div>
  <div class="edge-band"></div>

  <div class="person">
    <p class="person-name"><span class="first">Director</span> <span class="last">Name</span></p>
    <p class="person-role">Managing Director</p>
  </div>

  <ul class="contact-list">
    <li>
      <svg viewBox="0 0 12 12" aria-hidden="true"><path d="M6 0a4 4 0 0 0-4 4c0 3 4 8 4 8s4-5 4-8a4 4 0 0 0-4-4zm0 5.5A1.5 1.5 0 1 1 6 2.5a1.5 1.5 0 0 1 0 3z"/></svg>
      <span>48 Ridgeline Road, Maple Hollow,<br>WA 6999, Australia</span>
    </li>
    <li>
      <svg viewBox="0 0 12 12" aria-hidden="true"><path d="M2.5 0.5l2 2-1 1.5c.7 1.5 2 2.8 3.5 3.5l1.5-1 2 2-1.5 2C4.5 11.5.5 7.5.5 2z"/></svg>
      <span>0400 555 219</span>
    </li>
    <li>
      <svg viewBox="0 0 12 12" aria-hidden="true"><path d="M0 2h12v8H0z M0.5 2.5L6 7l5.5-4.5" fill="var(--navy)" stroke="#fff" stroke-width=".8"/></svg>
      <span>admin@korvellplantservices.net</span>
    </li>
  </ul>
</section>

</body>
</html>
```